Asia Hotel need a card and logo

The new hotel in East Asia, Taiwan need a business card and logo design.The hotel's Chinese name is 岚溪文旅,English name is "Virel Hotel".The core concept of this hotel is "Eco green", going to use many plant etc.,The building's first outlook draft is attached in the file for your reference.The style be modern and fashion will be good. Thank you.
Target Market(s)
East Asia
Industry/Entity Type
Hotel
Contact Information for Business Card
The hotel's name both in Chinese and English :岚溪商旅 Virel Hotel
The logo, address, E-mail and tel number place.
Stuff's name and title.
Font styles to use
Colors
Designer to choose colors to be used in the design.
Look and feel
Each slider illustrates characteristics of the customer's brand and the style your logo design should communicate.

```html
<!DOCTYPE html>
<html lang="en">
<head>
<meta charset="utf-8">
<title>Virel Hotel – Business Card</title>
<link href="https://fonts.googleapis.com/css2?family=Montserrat:wght@500;600;700&family=Arimo:wght@400&family=Noto+Sans+TC:wght@700&display=swap" rel="stylesheet">
<style>
  :root {
    --page: #e7e9e6;
    --green-light: #72c04a;
    --green: #22a046;
    --green-deep: #0f8a3e;
    --ink: #3a3a3a;
    --white: #ffffff;
    --icon-red: #e8262d;
  }
  * { box-sizing: border-box; margin: 0; padding: 0; }
  html, body { width: 1200px; height: 910px; overflow: hidden; }
  body {
    background: var(--page);
    display: flex;
    flex-direction: column;
    align-items: center;
    justify-content: center;
    gap: 40px;
    font-family: "Arimo", Arial, sans-serif;
  }
  .card {
    position: relative;
    width: 700px;
    height: 400px;
    border-radius: 26px;
    overflow: hidden;
    box-shadow: 0 10px 30px rgba(0,0,0,0.18);
  }

  /* back side */
  .card--back {
    background: linear-gradient(160deg, var(--green-light) 0%, var(--green) 55%, var(--green-deep) 100%);
    color: var(--white);
  }
  .card--back .wordmark {
    position: absolute;
    left: 0; right: 0; top: 130px;
    text-align: center;
  }
  .card--back .website {
    position: absolute;
    left: 0; right: 0; bottom: 90px;
    text-align: center;
    font-size: 14px;
    letter-spacing: 0.5px;
  }

  .wordmark-cn {
    display: block;
    font-family: "Noto Sans TC", sans-serif;
    font-weight: 700;
    font-size: 26px;
    line-height: 1.3;
    letter-spacing: 4px;
    margin-bottom: 4px;
  }
  .wordmark-en {
    display: inline-flex;
    align-items: center;
    gap: 14px;
    font-family: "Montserrat", sans-serif;
    font-weight: 700;
    font-size: 62px;
    line-height: 1;
  }
  .wordmark-dot {
    width: 22px; height: 22px; border-radius: 50%;
    background: currentColor;
    display: inline-block;
  }

  /* front side */
  .card--front { background: var(--white); }
  .card--front .wordmark {
    position: absolute;
    left: 120px; top: 60px;
    color: var(--green);
  }
  .card--front .wordmark-en { font-size: 56px; }
  .card--front .wordmark-cn { font-size: 23px; }

  .rule {
    position: absolute;
    height: 1.5px;
    background: var(--green);
  }
  .rule--top { left: 110px; right: 50px; top: 172px; }
  .rule--name { left: 50px; width: 300px; top: 270px; }

  .contact {
    position: absolute;
    right: 50px; top: 184px;
    list-style: none;
    text-align: right;
    color: var(--ink);
    font-size: 17px;
    line-height: 1.5;
  }
  .contact li { display: flex; align-items: center; justify-content: flex-end; gap: 12px; }
  .contact svg { width: 20px; height: 20px; flex: none; }

  .person {
    position: absolute;
    left: 50px; top: 280px;
    font-family: "Montserrat", sans-serif;
  }
  .person-name {
    font-weight: 700;
    font-size: 24px;
    letter-spacing: 1px;
    color: var(--ink);
  }
  .person-title {
    font-weight: 500;
    font-size: 20px;
    color: var(--green);
    letter-spacing: 0.5px;
  }

  .address-band {
    position: absolute;
    left: 0; right: 0; bottom: 0;
    height: 52px;
    background: linear-gradient(90deg, var(--green-deep), var(--green-light));
    color: var(--white);
    font-size: 18px;
    letter-spacing: 0.5px;
    display: flex;
    align-items: center;
    justify-content: center;
  }
</style>
</head>
<body>

  <section class="card card--back" aria-label="Card back">
    <div class="wordmark">
      <span class="wordmark-cn">岚溪商旅</span>
      <span class="wordmark-en"><span class="wordmark-dot"></span>Virel Hotel</span>
    </div>
    <p class="website">www.virelhotel.com</p>
  </section>

  <section class="card card--front" aria-label="Card front">
    <div class="wordmark">
      <span class="wordmark-cn">岚溪商旅</span>
      <span class="wordmark-en"><span class="wordmark-dot"></span>Virel Hotel</span>
    </div>

    <div class="rule rule--top"></div>

    <ul class="contact">
      <li>230.555.0147
        <svg viewBox="0 0 20 20" aria-hidden="true"><rect width="20" height="20" rx="4" fill="var(--icon-red)"/><path d="M6 4.5l2 2.5-1.2 1.5a7 7 0 0 0 4.7 4.7L13 12l2.5 2-1 1.8C9.5 16 4 10.5 4.2 5.5z" fill="#fff"/></svg>
      </li>
      <li>daniel@virelhotel.com
        <svg viewBox="0 0 20 20" aria-hidden="true"><rect width="20" height="20" rx="4" fill="var(--icon-red)"/><rect x="4" y="6" width="12" height="8.5" fill="none" stroke="#fff" stroke-width="1.5"/><path d="M4 6l6 5 6-5" fill="none" stroke="#fff" stroke-width="1.5"/></svg>
      </li>
      <li>www.virelhotel.com
        <svg viewBox="0 0 20 20" aria-hidden="true"><rect width="20" height="20" rx="4" fill="var(--icon-red)"/><circle cx="10" cy="10" r="5.5" fill="none" stroke="#fff" stroke-width="1.4"/><ellipse cx="10" cy="10" rx="2.4" ry="5.5" fill="none" stroke="#fff" stroke-width="1.2"/><path d="M4.5 10h11" stroke="#fff" stroke-width="1.2"/></svg>
      </li>
    </ul>

    <div class="rule rule--name"></div>
    <div class="person">
      <p class="person-name">DANIEL WHITMORE</p>
      <p class="person-title">CEO/FOUNDER</p>
    </div>

    <div class="address-band">4200 Harbor Park Ave, Ste 310, Lakemont, NC 28090</div>
  </section>

</body>
</html>
```